Acupuncture business needs business card design

I need a business card for an acupuncture clinic called "Summit Wellpath"
It will need the following details:
My name: Marcus Thelwick
Acupuncturist
Member KPTG
BVF Treatment Provider
Ph numbers: 482 1358 027 514 3820
Email: marcus@swpath.example.nz
On the back it will need a table with 2 columns for appointments, one column for time and one for date.

Industry/Entity Type

Clinic

Contact Information for Business Card

Marcus Thelwick
Acupuncturist
Member KPTG
BVF Treatment Provider
Email: marcus@swpath.example.nz

Requirements
Must have
• Marcus Thelwick
• Acupuncturist
• Member KPTG
• BVF Treatment Provider
• Ph numbers: 482 1358 027 514 3820
• Email: marcus@swpath.example.nz
• On the back it will need a table with 2 columns for appointments, one column for time and one for date.

```html
<!DOCTYPE html>
<html lang="en">
<head>
<meta charset="utf-8">
<title>Summit Wellpath – Business Card</title>
<link rel="stylesheet" href="https://fonts.googleapis.com/css2?family=Fira+Sans:wght@400;500;600;700&display=swap">
<style>
  :root {
    --backdrop: #2e2e2e;
    --paper: #ffffff;
    --teal: #0d6a86;
    --teal-deep: #0a5a73;
    --sky: #1c9fd6;
    --ink: #1d1d1d;
    --rule: #8a8a8a;
    --divider: rgba(255,255,255,0.55);
  }
  * { box-sizing: border-box; margin: 0; padding: 0; }
  html, body {
    width: 1200px; height: 1000px; overflow: hidden;
    background: var(--backdrop);
    font-family: "Fira Sans", sans-serif;
  }
  .sheet {
    width: 1200px; height: 1000px;
    display: flex; flex-direction: column; align-items: center; justify-content: center;
    gap: 48px;
  }
  .card {
    position: relative;
    width: 720px; height: 412px;
    background: var(--paper);
    overflow: hidden;
    box-shadow: 0 10px 30px rgba(0,0,0,0.45);
  }

  /* brand lockup */
  .brand {
    position: absolute;
    display: flex; align-items: center; gap: 14px;
  }
  .brand-dot {
    width: 34px; height: 34px; border-radius: 50%;
    background: var(--teal);
  }
  .brand-name {
    font-weight: 600; font-size: 40px; color: var(--sky);
    letter-spacing: -0.5px; line-height: 1;
  }

  /* front */
  .front .brand { left: 0; right: 0; top: 68px; justify-content: center; }
  .front-band {
    position: absolute; left: 0; right: 0; bottom: 0; height: 232px;
    background: radial-gradient(ellipse at 62% 55%, var(--teal) 0%, var(--teal-deep) 100%);
    color: #fff;
    display: flex; align-items: center;
  }
  .holder { width: 330px; padding-left: 90px; }
  .holder-name { font-weight: 600; font-size: 27px; margin-bottom: 8px; }
  .holder-role { font-size: 19px; line-height: 1.28; font-weight: 400; }
  .band-divider { width: 1px; height: 126px; background: var(--divider); margin: 0 42px 0 30px; }
  .contacts { list-style: none; display: flex; flex-direction: column; gap: 16px; font-size: 20px; }
  .contacts li { display: flex; align-items: center; gap: 12px; }
  .contact-icon {
    width: 22px; height: 22px; border-radius: 4px; background: var(--sky);
    display: flex; align-items: center; justify-content: center;
  }

  /* back */
  .back .brand { left: 0; right: 0; top: 48px; justify-content: center; }
  .back-title {
    position: absolute; left: 0; right: 0; top: 116px; text-align: center;
    font-weight: 600; font-size: 27px; color: var(--teal);
  }
  .appointments {
    position: absolute; left: 62px; right: 62px; top: 178px;
    display: flex; flex-direction: column; gap: 26px;
  }
  .slot { display: flex; align-items: flex-end; font-size: 19px; color: var(--ink); }
  .slot-label { white-space: nowrap; padding-right: 12px; }
  .slot-line { border-bottom: 1.5px solid var(--rule); height: 1px; margin-bottom: 4px; }
  .slot-line.date { flex: 1 1 auto; margin-right: 34px; }
  .slot-line.time { width: 150px; }
</style>
</head>
<body>
<main class="sheet">

  <section class="card front" aria-label="Business card front">
    <div class="brand">
      <span class="brand-dot"></span>
      <span class="brand-name">Summit Wellpath</span>
    </div>
    <div class="front-band">
      <div class="holder">
        <p class="holder-name">Marcus Thelwick</p>
        <p class="holder-role">Acupuncturist</p>
        <p class="holder-role">Member KPTG</p>
        <p class="holder-role">BVF Treatment Provider</p>
      </div>
      <div class="band-divider"></div>
      <ul class="contacts">
        <li>
          <span class="contact-icon">
            <svg width="14" height="14" viewBox="0 0 24 24"><path fill="#fff" d="M6.6 10.8a15.5 15.5 0 0 0 6.6 6.6l2.2-2.2c.3-.3.7-.4 1-.2 1.1.4 2.3.6 3.6.6.6 0 1 .4 1 1V20c0 .6-.4 1-1 1A17 17 0 0 1 3 4c0-.6.4-1 1-1h3.5c.6 0 1 .4 1 1 0 1.3.2 2.5.6 3.6.1.3 0 .7-.2 1l-2.3 2.2z"/></svg>
          </span>482 1358
        </li>
        <li>
          <span class="contact-icon">
            <svg width="14" height="14" viewBox="0 0 24 24"><path fill="#fff" d="M6.6 10.8a15.5 15.5 0 0 0 6.6 6.6l2.2-2.2c.3-.3.7-.4 1-.2 1.1.4 2.3.6 3.6.6.6 0 1 .4 1 1V20c0 .6-.4 1-1 1A17 17 0 0 1 3 4c0-.6.4-1 1-1h3.5c.6 0 1 .4 1 1 0 1.3.2 2.5.6 3.6.1.3 0 .7-.2 1l-2.3 2.2z"/></svg>
          </span>027 514 3820
        </li>
        <li>
          <span class="contact-icon">
            <svg width="14" height="12" viewBox="0 0 24 20"><rect x="1" y="2" width="22" height="16" rx="2" fill="#fff"/><path d="M2 3l10 8 10-8" fill="none" stroke="#1c9fd6" stroke-width="2"/></svg>
          </span>marcus@swpath.example.nz
        </li>
      </ul>
    </div>
  </section>

  <section class="card back" aria-label="Business card back">
    <div class="brand">
      <span class="brand-dot"></span>
      <span class="brand-name">Summit Wellpath</span>
    </div>
    <h2 class="back-title">Your Next Appointment</h2>
    <div class="appointments">
      <div class="slot"><span class="slot-label">Day/Date</span><span class="slot-line date"></span><span class="slot-label">Time</span><span class="slot-line time"></span></div>
      <div class="slot"><span class="slot-label">Day/Date</span><span class="slot-line date"></span><span class="slot-label">Time</span><span class="slot-line time"></span></div>
      <div class="slot"><span class="slot-label">Day/Date</span><span class="slot-line date"></span><span class="slot-label">Time</span><span class="slot-line time"></span></div>
      <div class="slot"><span class="slot-label">Day/Date</span><span class="slot-line date"></span><span class="slot-label">Time</span><span class="slot-line time"></span></div>
    </div>
  </section>

</main>
</body>
</html>
```